New look and feel for investment website

Hi

Our website needs a crisp and professional look and feel applying to it. Here’s the address: http://www.brightplinth.co.uk. Since posting the brief yesterday (Tuesday, 16 August), we've reduced the amount of content on the home page, which should make life a little easier for you. We will come back later today, with some points of reference in terms of sites we like the look of. (See below)

17 August, 1.20pm GMT. OK, comments generally on the designs submitted so far. Please keep in mind that images of graphs, piles of coins, paper money and pretty females are not what is required. Better to think in terms of abstract imagery instead. Ratios? Circles? Relationships? Patterns? Not money,sex,graphs etc. Hope that helps.

For guidance on look and feel, please refer to these sites, which we like:

http://www.morvelle.co.uk/
http://www.qz.com/
https://www.harrowfieldtamsin.com
https://www.pirelconcerns.com
https://www.kvantule.com
Updates

Here's the Tall Beacons logo created in AI CS5.

Our market is professional financial advisers and relatively sophisticated private investors. The look and feel therefore should be slick and sophisticated - not 'lively' and lightweight, more like a banking site. Please read the brief again where we've added a list of websites that we really like the look of to get a better feel for what we're looking for. Thanks once again, we appreciate the work you're putting in.

It's essential that all the elements that are on the current home page be included on all new designs. 

We use a device in our e-mails which you may wish to incorporate in your design.

Target Market(s)

Professional financial advisers. People who know about investment and money.

Industry/Entity Type

Investment

Requirements
Should not have
• Graphs or people.

```html
<!DOCTYPE html>
<html lang="en">
<head>
<meta charset="utf-8">
<title>Tall Beacons — Value Investing</title>
<link rel="stylesheet" href="https://fonts.googleapis.com/css2?family=Montserrat:wght@400;500&family=Open+Sans:wght@400;600;700&family=PT+Serif&display=swap">
<style>
:root{
  --ink:#1d3a48;
  --ink-dark:#12262f;
  --red:#e8202a;
  --text:#333;
  --grey:#777;
  --panel:#efefef;
  --rule:#bdbdbd;
}
*{box-sizing:border-box;margin:0;padding:0}
html,body{width:960px;height:1200px;overflow:hidden;background:#fff}
body{position:relative;font-family:'Open Sans',sans-serif;color:var(--text)}
.abs{position:absolute}
.topbar{left:0;top:0;width:960px;height:29px;background:linear-gradient(#2c5566,#1d3f4d)}
.topbar a{position:absolute;top:8px;font-size:9px;color:#fff;text-decoration:none}
.brand{left:96px;top:48px;font-family:'Montserrat',sans-serif;font-size:28px;color:#666;font-weight:400;display:flex;align-items:center;gap:6px}
.brand i{width:6px;height:6px;background:var(--red);display:inline-block}
.tagline{left:478px;top:46px;width:400px;font-family:'Montserrat',sans-serif;font-size:13.3px;line-height:19px;color:var(--ink-dark)}
.tagline em{font-style:normal;color:var(--red)}
.rule{left:96px;width:768px;height:1px;background:#999}
.mainnav{left:96px;top:110px;width:768px;display:flex;justify-content:space-between;padding:0 10px}
.mainnav a{display:flex;flex-direction:column;align-items:center;gap:4px;font-size:9px;color:#555;text-decoration:none;letter-spacing:.2px}
.mainnav svg{width:13px;height:13px;fill:var(--ink)}
.hero{left:96px;top:177px;width:768px;height:285px;background:linear-gradient(100deg,#5f8a98 0%,#2b4f5c 45%,#0f2530 100%);overflow:hidden}
.hero-art{left:0;top:118px;width:256px;height:150px;background:radial-gradient(circle at 0 100%,#6a1020 0%,#3a0710 60%,#200408 100%);border:4px solid #222;border-bottom-width:6px}
.hero-title{left:337px;top:92px;font-family:'Montserrat',sans-serif;font-size:19px;line-height:24px;color:#fff}
.cta{left:334px;top:157px;width:186px;height:34px;background:linear-gradient(#fff,#e6e6e6);border-radius:4px;display:flex;align-items:center;justify-content:space-between;padding:0 20px 0 13px;font-family:'Montserrat',sans-serif;font-size:15px;color:var(--red);text-decoration:none}
.cta svg{width:11px;height:13px}
.hero-note{left:534px;top:166px;font-family:'Montserrat',sans-serif;font-size:13px;line-height:17px;color:#fff}
.hero-note b{font-weight:500}
h2{font-family:'Montserrat',sans-serif;font-weight:400;color:var(--red)}
.lead-h{left:138px;top:489px;width:320px;font-size:14.3px;line-height:19px}
.lead-icon{left:96px;top:494px;width:32px;height:46px}
.serif{font-family:'PT Serif',serif;font-size:9.4px;line-height:16px;color:#333;text-align:justify}
.col-l{left:96px;width:358px}
.col-r{left:493px;width:368px}
.statement{font-family:'Montserrat',sans-serif;font-weight:500;font-size:11.8px;line-height:17px;color:var(--ink)}
.more{left:493px;top:759px;font-size:10.6px;color:var(--red);text-decoration:none;border-bottom:1px solid var(--red);padding-bottom:4px;display:flex;gap:8px;align-items:center;width:342px}
.stats{left:96px;top:821px;width:768px;height:229px;background:var(--panel);border-top:1px solid #ccc;border-bottom:1px solid #ccc}
.val{position:absolute;font-family:'Montserrat',sans-serif;font-size:13.5px;color:var(--red);text-align:center;width:90px}
.cap{position:absolute;font-size:9.5px;line-height:11px;color:#333;text-align:center;width:80px}
.bar{position:absolute;width:28px;background:linear-gradient(var(--ink),var(--ink-dark));border-bottom:2px solid var(--red)}
.num{position:absolute;left:430px;width:42px;height:42px;border-radius:50%;background:var(--ink-dark);color:#fff;font-family:'Montserrat',sans-serif;font-size:17px;display:flex;align-items:center;justify-content:center}
.fact{position:absolute;left:491px;width:270px;font-size:9.6px;line-height:11px;color:var(--ink);border-bottom:1px dashed #999;padding-bottom:5px}
.trade{position:absolute;font-size:9.5px;color:#333}
.tbar{position:absolute;height:5px}
.rate{left:435px;top:202px;font-family:'Montserrat',sans-serif;font-size:15px;color:var(--red)}
.contact{left:96px;top:1068px;width:768px;font-size:8.5px;line-height:13px;font-weight:700;color:#333}
.legal{left:96px;top:1121px;width:768px;font-size:7.3px;line-height:11.2px;color:#444}
</style>
</head>
<body>
<nav class="abs topbar">
  <a style="left:98px">Home</a><a style="left:147px">Login</a><a style="left:194px">Register for free</a><a style="left:291px">Contact us</a><a style="left:362px">Terms &amp; Conditions</a>
</nav>

<div class="abs brand"><span>Tall Beacons</span><i></i></div>
<p class="abs tagline">A potential return of <em>23.57 %</em> a year from America's biggest businesses&nbsp; with the emphasis firmly on capital preservation.</p>

<div class="abs rule" style="top:104px"></div>
<nav class="abs mainnav">
  <a><svg viewBox="0 0 16 16"><circle cx="8" cy="8" r="6.5" fill="none" stroke="#1d3a48" stroke-width="1.8"/><path d="M7.2 4h1.6v4.2H11v1.5H7.2z"/></svg>2 Minute Guide</a>
  <a><svg viewBox="0 0 16 16"><rect x="1" y="9" width="3" height="6"/><rect x="5" y="6" width="3" height="9"/><rect x="9" y="3" width="3" height="12"/><rect x="13" y="1" width="2.5" height="14"/></svg>Performance</a>
  <a><svg viewBox="0 0 16 16"><path d="M1 8c2-4 12-4 14 0-2 4-12 4-14 0z" fill="none" stroke="#1d3a48" stroke-width="1.5"/><circle cx="8" cy="8" r="2.3"/></svg>Watchlist</a>
  <a><svg viewBox="0 0 16 16"><rect x="2" y="3" width="12" height="12" rx="1"/><path d="M5 11l5-5 1 1-5 5H5z" fill="#fff"/></svg>Key Numbers</a>
  <a><svg viewBox="0 0 16 16"><path d="M7 2a6.5 6.5 0 1 0 6.5 7H7z"/><path d="M9 0.5V7h6.5A6.5 6.5 0 0 0 9 .5z"/></svg>Results</a>
  <a><svg viewBox="0 0 16 16"><path d="M1 15V9l3-3 2 4 3-8 2 5 2-3 2 5v6z"/></svg>Trading History</a>
  <a><svg viewBox="0 0 16 16"><circle cx="6.5" cy="6.5" r="4.5" fill="none" stroke="#1d3a48" stroke-width="2"/><path d="M9.5 10.5l1.5-1.5 4.5 4.5-1.5 1.5z"/></svg>FAQs</a>
  <a><svg viewBox="0 0 16 16"><circle cx="6" cy="6" r="4"/><circle cx="12" cy="12" r="3"/></svg>Analysis</a>
  <a><svg viewBox="0 0 16 16"><text x="8" y="14" text-anchor="middle" font-size="15" font-weight="700" font-family="Open Sans">$</text></svg>Value Investing</a>
  <a><svg viewBox="0 0 16 16"><path d="M1 1v14h14" fill="none" stroke="#1d3a48" stroke-width="1.5"/><path d="M3 11l4-4 3 3 5-6" fill="none" stroke="#1d3a48" stroke-width="1.5"/></svg>Halden 1000 &amp; Verity 500</a>
</nav>
<div class="abs rule" style="top:150px"></div>

<section class="abs hero">
  <div class="abs hero-art" role="img" aria-label="Laptop showing abstract concentric red arcs with scattered coloured dots over a blurred city walkway photograph"></div>
  <h1 class="abs hero-title" style="font-weight:400">We use Custom Software to analyse<br>and identify undervalued stocks</h1>
  <a class="abs cta">Register for Free <svg viewBox="0 0 11 13"><path d="M2 1l7 5.5L2 12" fill="none" stroke="#1d3a48" stroke-width="2.5"/></svg></a>
  <p class="abs hero-note">Monitor our service<br><b>free of charge for six months</b></p>
</section>

<svg class="abs lead-icon" viewBox="0 0 32 46"><g fill="#aaa"><rect x="0" y="24" width="6" height="6"/><rect x="10" y="17" width="6" height="6"/><rect x="20" y="4" width="6" height="6"/><rect x="26" y="0" width="6" height="6"/><rect x="0" y="34" width="32" height="2"/><rect x="0" y="39" width="32" height="2"/><rect x="0" y="44" width="32" height="2"/></g><path d="M3 27L13 20L23 7" fill="none" stroke="#aaa" stroke-width="1.5"/></svg>
<h2 class="abs lead-h">A methodical, consistent, highly selective system-driven process for identifying, and investing in, undervalued stocks.</h2>
<p class="abs serif col-l" style="top:552px">The attractions of value investing need no explanation to those who subscribe to the concept. But it's impractical, if not impossible, for the private investor to implement the strategy (using direct holdings as distinct to collective funds) consistently. Although the data may be available, to undertake fundamental analysis regularly, on a reasonable number of stocks, entails a significant amount of time and effort.</p>
<p class="abs serif col-l" style="top:648px">By definition - and depending on where you look and market conditions - undervalued businesses (stocks) are relatively scarce. So where does the value investor begin their search? Which and how many businesses must be scrutinised before one undervalued entity is found? And having identified a stock that's trading at less than its fair value, will that be the case next week or next month? Fundamentals can change for the worse at any time, so without the benefit of regular analysis, how will the value investor know when to disinvest?</p>
<p class="abs statement col-l" style="top:768px">Those problems - and others - are now solved. Our software produces the quantitative analysis value investors need.</p>

<h2 class="abs" style="left:492px;top:487px;font-size:14.3px">Here's what we do:</h2>
<p class="abs serif col-r" style="top:513px">Once a month, month in month out, our program scrutinises the key fundamentals of 1,000 large cap American companies which between them account for 92% of the US securities market.</p>
<p class="abs serif col-r" style="top:577px">First of all, the program sifts through each of the 1,000 stocks searching for favourable arrays of fundamentals: that process usually filters out between 950 and 975 stocks. The software then applies a range of algorithms to the short-listed stocks to identify any which are trading at 35% (or more) below their estimated fair value. There are times when not one single stock on the shortlist satisfies that criteria. But when they do - and if there's room - those stocks are added to our portfolio.</p>
<p class="abs statement col-r" style="top:690px">We're not stock pickers, share tippers or brokers. What we do is use software to analyse and identify stocks that appear to be undervalued.</p>
<a class="abs more">More about value investing - the investment strategy we follow <svg width="18" height="8" viewBox="0 0 18 8"><path d="M0 4h16M12 0.5l4 3.5-4 3.5" fill="none" stroke="#333" stroke-width="1.2"/></svg></a>

<section class="abs stats">
  <div class="val" style="left:8px;top:81px">23.57 %</div>
  <div class="val" style="left:80px;top:103px">13.49 %</div>
  <div class="val" style="left:143px;top:130px">-1.48 %</div>
  <div class="val" style="left:209px;top:13px">69.77 %</div>
  <div class="val" style="left:289px;top:83px">24.44 %</div>
  <div class="bar" style="left:32px;top:107px;height:44px"></div>
  <div class="bar" style="left:104px;top:125px;height:26px"></div>
  <div class="bar" style="left:170px;top:151px;height:6px"></div>
  <div class="bar" style="left:240px;top:49px;height:102px"></div>
  <div class="bar" style="left:315px;top:107px;height:44px"></div>
  <div class="abs" style="left:11px;top:151px;width:372px;height:1px;background:#555"></div>
  <div class="cap" style="left:5px;top:164px">Average, annualised compound return:</div>
  <div class="cap" style="left:78px;top:164px">YTD Portfolio Return</div>
  <div class="cap" style="left:144px;top:164px">Highest annual loss</div>
  <div class="cap" style="left:214px;top:164px">Highest annual gain</div>
  <div class="cap" style="left:291px;top:164px">Average return per trade</div>

  <div class="num" style="top:12px"><span>11</span><span style="font-size:13px">/4</span></div>
  <div class="num" style="top:62px">5</div>
  <div class="num" style="top:112px">287</div>
  <p class="fact" style="top:29px">Maximum number of winning/losing trades in a row</p>
  <p class="fact" style="top:71px">The average number of trades a yearand never more than five holdings at any one time</p>
  <p class="fact" style="top:129px;width:274px">The average number of days a stock stays in the portfolio</p>
  <span class="trade" style="left:436px;top:169px">86 trades</span>
  <div class="tbar" style="left:493px;top:173px;width:268px;background:var(--red)"></div>
  <span class="trade" style="left:436px;top:184px">65 were profitable</span>
  <div class="tbar" style="left:553px;top:188px;width:208px;background:var(--ink-dark)"></div>
  <p class="abs rate">75.5 % success rate</p>
</section>

<p class="abs contact">If you have any questions, please e-mail info@tallbeacons.co.uk. Although we're very willing to answer queries about the way we pick stocks, please do keep in mind that as we're giving this service away free of charge initially, we're not inclined to expend time and energy debating the relative merits of value investing or fundamental analyses. Other than that, fire away!</p>
<p class="abs legal">This website is published by Tall Beacons Ltd. Registered in England No. 08314726. Registered office: 41 Larkfield Row London N9 2QT. This website and its content is the copyright of Tall Beacons Ltd - © Tall Beacons Ltd 2011. All rights reserved. Any redistribution or reproduction of part or all of the contents in any form is prohibited other than the following: you may print or download to a local hard disk extracts for your personal and non-commercial use only you may copy the content to individual third parties for their personal use, but only if you acknowledge the website as the source of the material. You may not, except with our express written permission, distribute or commercially exploit the content. Nor may you transmit it or store it in any other website or other form of electronic retrieval system.</p>
</body>
</html>
```